Property Management Firm Introduces New Programs

4 pages, 5.5 x 8.5 finished size, 4-color
We are introducing two new programs: Financial Management and K-Steer. These programs are more affordable than full-service management. The brochure should come across as professional but not too glossy to give the impression of affordability coupled with stability and reliability. That said, we like to have a little fun with what we do--or it's not worth doing.

Target Market(s)

self-managed HOA and condo association

Industry/Entity Type

Real Estate

Other font styles liked:
• Trocchi, Activ Grotesk

Requirements
Must have
• Easy to read
• Our corporate fonts are Trocchi and Aktiv Grotesk
• Let me know if you need me to upload those fonts.
• LOGO Colors
• Red / Green / Blue
• Cyan 27 84 74
• Magenta 98 25 75
• Yellow 81 96 3
• Black 49 28 85
Nice to have
• The content is submitted in a rough design format to give you an idea of what we are looking for. I've attached the photos used in the design. Am open to the idea of different photos. This has a tight deadline so trying to give as much as possible

```html
<!DOCTYPE html>
<html lang="en">
<head>
<meta charset="utf-8">
<title>Financial Management and K-Steer brochure spread</title>
<link href="https://fonts.googleapis.com/css2?family=Trocchi&family=Roboto+Condensed:wght@300;400;500&display=swap" rel="stylesheet">
<style>
  :root {
    --maroon: #8b2335;
    --maroon-dark: #6e1626;
    --maroon-light: #a8394b;
    --ink: #5a5a5a;
    --rule-grey: #7a7a7a;
    --paper: #ffffff;
    --paper-shade: #ececec;
    --backdrop: #d6d6d6;
    --gold-1: #c9a667;
    --gold-2: #8c6b3a;
    --gold-3: #e4cf9d;
  }
  * { box-sizing: border-box; margin: 0; padding: 0; }
  html, body { width: 1200px; height: 801px; overflow: hidden; }
  body {
    background: var(--backdrop);
    font-family: "Roboto Condensed", "Arial Narrow", sans-serif;
    color: var(--ink);
  }
  .spread {
    position: absolute;
    left: 75px; top: 20px;
    width: 1050px; height: 760px;
    display: flex;
  }
  .page {
    position: relative;
    width: 525px; height: 760px;
    background: var(--paper);
    overflow: hidden;
  }
  .page--left { background: linear-gradient(to right, #fafafa 0%, #fff 80%, var(--paper-shade) 100%); }
  .page--right { background: linear-gradient(to left, #fafafa 0%, #fff 80%, var(--paper-shade) 100%); }

  .section-band {
    position: absolute; left: 0; right: 0;
    height: 33px;
    background: linear-gradient(to bottom, var(--maroon-light), var(--maroon) 60%, var(--maroon-dark));
  }
  .page--left .section-band { top: 24px; }
  .page--right .section-band { top: 30px; height: 30px; }
  .section-title {
    position: absolute; top: 50%; transform: translateY(-50%);
    font-family: "Trocchi", Georgia, serif;
    color: #fff; font-size: 18px; letter-spacing: 0.5px;
    text-transform: uppercase;
  }
  .page--left .section-title { left: 48px; }
  .page--right .section-title { left: 47px; }

  .coin-photo {
    position: absolute; left: 0; right: 0; top: 57px; height: 133px;
    background: linear-gradient(160deg, var(--gold-3) 0%, var(--gold-1) 35%, var(--gold-2) 70%, #b5925a 100%);
  }
  .service-pin { position: absolute; left: 360px; top: 60px; width: 112px; height: 168px; }

  .mouse-art {
    position: absolute; left: 372px; top: 10px; width: 135px; height: 88px;
    border-radius: 50% 50% 45% 45%;
    background: radial-gradient(ellipse at 40% 40%, #e7a3a3 0%, #c95b5b 45%, #a8a8a8 80%, #e0e0e0 100%);
  }

  .heading {
    position: absolute;
    font-family: "Trocchi", Georgia, serif;
    font-size: 19px; color: var(--maroon);
    padding-left: 17px;
  }
  .heading::before {
    content: ""; position: absolute; left: 0; top: 1px;
    width: 8px; height: 24px; background: var(--rule-grey);
  }
  .page--left .heading { left: 32px; top: 219px; }

  .body-copy { font-size: 12.6px; line-height: 16.2px; font-weight: 300; }

  .bullets { list-style: none; position: absolute; }
  .bullets li { position: relative; padding-left: 22px; }
  .bullets li::before {
    content: ""; position: absolute; left: 0; top: 5px;
    border-left: 6px solid var(--maroon);
    border-top: 3.5px solid transparent; border-bottom: 3.5px solid transparent;
  }
  .benefits { left: 50px; top: 253px; width: 424px; text-align: justify; }
  .benefits li { margin-bottom: 16.3px; }

  .page--right .heading { left: 30px; }
  .intro { position: absolute; left: 47px; width: 432px; }
  .subhead {
    position: absolute; left: 47px; width: 440px;
    font-weight: 500; color: var(--maroon); font-size: 14.5px; line-height: 19px;
  }
  .functions, .extras { left: 47px; width: 440px; }
  .support-badge { position: absolute; left: 388px; top: 614px; width: 104px; height: 104px; }

  .foot-band { position: absolute; left: 0; bottom: 0; width: 525px; height: 48px; }
</style>
</head>
<body>
<main class="spread">

  <section class="page page--left">
    <header class="section-band"><h1 class="section-title">Financial Management</h1></header>
    <div class="coin-photo" role="img" aria-label="Photograph of stacked gold coins"></div>
    <svg class="service-pin" viewBox="0 0 112 168" aria-hidden="true">
      <path d="M56 4 A52 52 0 0 1 100 84 L56 164 L12 84 A52 52 0 0 1 56 4 Z" fill="#c4303e" opacity="0.88"/>
      <circle cx="56" cy="56" r="44" fill="#d8424f" opacity="0.9"/>
      <text x="56" y="52" text-anchor="middle" font-family="Roboto Condensed, sans-serif" font-size="17" font-weight="500" fill="#fff">FINANCIAL</text>
      <text x="56" y="72" text-anchor="middle" font-family="Roboto Condensed, sans-serif" font-size="17" font-weight="500" fill="#fff">SERVICES</text>
    </svg>

    <h2 class="heading">What do you get?</h2>
    <ul class="bullets benefits body-copy">
      <li>Whether your residents pay by check or electronically payments are posted daily and deposited to your dedicated operating account.</li>
      <li>Monthly reports, including balance sheet, income statement, budget comparison, disbursement register, delinquency report, copies of invoices, bank statements and reconciliation reports, all delivered by the 15th to a secure online portal with board-restricted access.</li>
      <li>Online approval of invoices with approval criteria you set. Once approved, payments are issued to vendors either electronically or by digitally-signed check. Board approvers can view the invoice, the GL code and bank account before payment is issued.</li>
      <li>Collections managed in conjunction with your attorney with Crestline monitoring action taken or not taken and a concise, case-by-case report included with your financials. Late fees are applied and late notices are issued by Crestline. The board and your attorney will have access to payment histories online.</li>
      <li>Audit &amp; tax support provided to your CPA either in our office or electronically. We will issue vendor 1099s and manage the filing of personal property returns, county registrations and tax returns.</li>
      <li>We will process property transfers, bankruptcies.</li>
      <li>A secure, online portal where your members can view their statements in real-time on computer, phone or tablet, and make online payments by automatic ACH payment, e-check or credit card (credit card fees apply).</li>
    </ul>

    <svg class="foot-band" viewBox="0 0 525 48" preserveAspectRatio="none" aria-hidden="true">
      <path d="M0 27 H360 C378 27 380 12 400 12 H525 V48 H0 Z" fill="var(--maroon)"/>
    </svg>
  </section>

  <section class="page page--right">
    <header class="section-band"><h1 class="section-title">K-Steer</h1></header>
    <div class="mouse-art" role="img" aria-label="Illustration of a red computer mouse"></div>

    <h2 class="heading" style="top:77px">What do you get?</h2>
    <p class="intro body-copy" style="top:116px">All the financial management services and options, PLUS the power of our robust management software to help with all your administrative needs.</p>
    <p class="intro body-copy" style="top:165px">With our K-Steer program, you or your staff will manage the portal. We can turn functions on or off to suit your needs—there is no cost to add functions.</p>

    <p class="subhead" style="top:214px">Some of the administrative functions you will have available include:</p>
    <ul class="bullets functions body-copy" style="top:236px">
      <li>Templated board meeting agendas and minutes</li>
      <li>Documents storage</li>
      <li>Managing maintenance requests</li>
      <li>Conducting covenants inspections and issuing violation notices</li>
      <li>Managing the architectural change request process</li>
      <li>Issuing mass communications to your residents via U.S. Mail, email, pop-up messages or texts.</li>
      <li>Managing clubhouse rental schedules</li>
      <li>A Crestline coordinator to help with questions and training for your Board and homeowners.</li>
    </ul>
    <p class="intro body-copy" style="top:414px">When these functions are activated, your residents will enjoy added convenience as well as open and interactive communications with your board, which leads to trust, confidence and, ultimately, a more engaged community.</p>

    <h2 class="heading" style="top:504px">What else do you get?</h2>
    <p class="subhead" style="top:532px">Certain a la carte services and hourly consulting are made available for a fee to our K-Steer clients. These include:</p>
    <ul class="bullets extras body-copy" style="top:581px">
      <li>Issuance of resale disclosures, lender questionnaires and payoff requests</li>
      <li>Annual meeting administration</li>
      <li>Budget assistance</li>
      <li>Credit reporting</li>
      <li>Covenants enforcement</li>
      <li>Project management</li>
      <li>Insurance claims management</li>
    </ul>

    <div class="support-badge" role="img" aria-label="Round gold and red support badge">
      <svg viewBox="0 0 104 104" width="104" height="104" aria-hidden="true">
        <circle cx="52" cy="52" r="50" fill="#d9b13c"/>
        <circle cx="52" cy="52" r="42" fill="var(--maroon)"/>
      </svg>
    </div>

    <svg class="foot-band" viewBox="0 0 525 48" preserveAspectRatio="none" aria-hidden="true">
      <path d="M0 12 H115 C135 12 137 27 155 27 H525 V48 H0 Z" fill="var(--maroon)"/>
    </svg>
  </section>

</main>
</body>
</html>
```